Business cards need a revamp and change of address. I have included files of current card which has been used for 5 years. Also a photo of my new store fitout which uses a lot of colour and features inspired by cusco Peru. I would like to see design options with and without the butterfly although I do use the butterfly on my current street signage.

Reason: would like to see more designers submit

Target Market(s)

women 35 - 65

Industry/Entity Type

Business

Contact Information for Business Card

Tawra Andean Silver Jewellery & Giftware

Requirements
Must have
• logo frontside
• backside the following text:
• Tawra Jewellery is hand made using the highest quality 950 Peruvian Silver which is purer than 925 Sterling Silver. Tawra's range of unique, handcrafted products are directly sourced from fair trade producer co-operatives, individual artisans and artisan groups from Peru, South America.
• Phone 02 63172846
• 7/118 Marlow Lane Kelby NSW 2861
• Email : sales@tawra-example.com.au
Nice to have
• Like us on face book

```html
<!DOCTYPE html>
<html lang="en">
<head>
<meta charset="utf-8">
<title>Tawra Business Card – Front and Back</title>
<link href="https://fonts.googleapis.com/css2?family=Dosis:wght@400;500;600&display=swap" rel="stylesheet">
<style>
  :root {
    --page-bg: #ecebe8;
    --card-bg: #ffffff;
    --ink: #1d1d1d;
    --ink-soft: #333333;
    --accent-blue: #1f5fc9;
    --logo-wash: #edf2f4;
    --card-shadow: rgba(0, 0, 0, 0.18);
  }
  * { box-sizing: border-box; margin: 0; padding: 0; }
  html, body {
    width: 1200px;
    height: 988px;
    overflow: hidden;
    background: var(--page-bg);
    font-family: "Dosis", sans-serif;
    color: var(--ink);
  }
  .canvas {
    position: relative;
    width: 1200px;
    height: 988px;
    display: flex;
    align-items: center;
    justify-content: center;
    gap: 60px;
  }
  .card {
    position: relative;
    width: 520px;
    height: 297px;
    background: var(--card-bg);
    box-shadow: 0 10px 28px var(--card-shadow);
  }
  /* Front */
  .card-front {
    display: flex;
    align-items: center;
    justify-content: center;
  }
  .logo-wash {
    width: 300px;
    height: 236px;
    border-radius: 50%;
    background: var(--logo-wash);
    display: flex;
    align-items: center;
    justify-content: center;
  }
  .brand-name {
    font-size: 64px;
    font-weight: 600;
    color: var(--ink);
    letter-spacing: 1px;
  }
  /* Back */
  .card-back { padding: 30px 32px 0; }
  .back-title {
    text-align: center;
    font-size: 36px;
    font-weight: 500;
    color: var(--accent-blue);
    line-height: 1;
    margin-bottom: 10px;
  }
  .back-intro {
    text-align: center;
    font-size: 11.5px;
    line-height: 1.35;
    color: var(--ink-soft);
    font-weight: 500;
  }
  .contact-main {
    position: absolute;
    left: 40px;
    bottom: 34px;
  }
  .contact-online {
    position: absolute;
    right: 30px;
    bottom: 96px;
  }
  .contact-row {
    display: flex;
    align-items: center;
    gap: 6px;
    color: var(--ink);
  }
  .contact-phone { font-size: 24px; font-weight: 500; margin-bottom: 4px; }
  .contact-address { font-size: 14px; }
  .contact-online .contact-row { font-size: 11px; line-height: 1.45; }
  .icon { flex: none; }
</style>
</head>
<body>
<main class="canvas">
  <section class="card card-front" aria-label="Card front">
    <div class="logo-wash">
      <span class="brand-name">tawra</span>
    </div>
  </section>

  <section class="card card-back" aria-label="Card back">
    <h1 class="back-title">Peruvian Silver</h1>
    <p class="back-intro">Tawra Jewellery is hand made using the highest quality 950 Peruvian Silver which is purer than 925 Sterling Silver. Tawra's range of unique, handcrafted products are directly sourced from fair trade producer co-operatives, individual artisans and artisan groups from Peru, South America.</p>

    <div class="contact-online">
      <div class="contact-row">
        <svg class="icon" width="11" height="9" viewBox="0 0 11 9" aria-hidden="true"><rect x="0.5" y="0.5" width="10" height="8" fill="none" stroke="currentColor"/><path d="M0.5 0.5 L5.5 5 L10.5 0.5" fill="none" stroke="currentColor"/></svg>
        <span>sales@tawra-example.com.au</span>
      </div>
      <div class="contact-row">
        <svg class="icon" width="11" height="11" viewBox="0 0 11 11" aria-hidden="true"><circle cx="5.5" cy="5.5" r="4.8" fill="none" stroke="currentColor"/><path d="M0.7 5.5 H10.3 M5.5 0.7 C3 3 3 8 5.5 10.3 M5.5 0.7 C8 3 8 8 5.5 10.3" fill="none" stroke="currentColor" stroke-width="0.8"/></svg>
        <span>www.tawra-example.com.au</span>
      </div>
      <div class="contact-row">
        <svg class="icon" width="11" height="11" viewBox="0 0 11 11" aria-hidden="true"><rect width="11" height="11" fill="var(--accent-blue)"/></svg>
        <span>Like us</span>
      </div>
    </div>

    <div class="contact-main">
      <div class="contact-row contact-phone">
        <svg class="icon" width="20" height="20" viewBox="0 0 20 20" aria-hidden="true"><path d="M4 2 L7 2 L8 6 L6 7.5 C7 10 9.5 12.5 12 13.5 L13.5 11.5 L17.5 12.5 L17.5 15.5 C17.5 17 16 18 14.5 17.8 C8.5 17 3 11.5 2.2 5.5 C2 4 3 2 4 2 Z" fill="currentColor"/></svg>
        <span>02 63172846</span>
      </div>
      <div class="contact-row contact-address">
        <svg class="icon" width="18" height="14" viewBox="0 0 18 14" aria-hidden="true"><path d="M9 1 C6.8 1 5.5 2.6 5.5 4.3 C5.5 6.5 9 9.5 9 9.5 C9 9.5 12.5 6.5 12.5 4.3 C12.5 2.6 11.2 1 9 1 Z" fill="none" stroke="currentColor" stroke-width="1.3"/><path d="M5 9 L1 13 H17 L13 9" fill="none" stroke="currentColor" stroke-width="1.3"/></svg>
        <span>7/118 Marlow Lane Kelby NSW 2861</span>
      </div>
    </div>
  </section>
</main>
</body>
</html>
```